Design eines Zertifikats
Ich bin total begeistert. Super Kommunikation, super schnelle Reaktion auf kleine Änderungswünsche, ich bin wirklich rundum zufrieden!! Auch bei weiterführenden Fragen die gar nicht direkt mit dem Design zusammenhingen wurde mir total schnell und sympathisch geholfen, ich kann die Designerin nur wärmstens weiterempfehlen!
Zielgruppe
Ich betreibe einen Onlineshop, in dem ich sogenannte Sterntaufen verkaufe. Ein Kunde bekommt dabei im Zuge seines Kaufes ein Zertifikat ausgestellt mit Daten zu seinem getauften Stern. Es geht hier um das Design eines neuen Zertifikats um möglichst noch mehr Käufer anzusprechen. Es sind bereits 3 Designs vorhanden, das neue sollte sich entsprechend etwas absetzen.
Ich lasse die Zertifikate in einer Druckerei drucken, und bedrucke diese dann selber mit den Daten der Sterntaufe, es muss auf dem Zertifikat also ein heller Bereich vorhanden sein in dem ich drucken kann.
Aufgabenstellung
Das Zertifikat soll A4 sein. Es sollte modern sein und sich wie gesagt möglichst von den bestehenden absetzen, und ein möglichst breites Publikum ansprechen.
Beispiele für Zertifikate der Konkurrenz finden sich unter:
lichtpunkt-shop.de
nebelbuchung.de
himmelsgabe-online.de
Das von lichtpunkt-shop.de gefällt mir persönlich ganz gut, aber lasst euch nicht von den Vorschlägen einschränken.
Bitte nicht zu exzessiv kostenpflichtiges Stockmaterial verwenden, ich mache leider aktuell noch Miese mit dem Shop :-)
Bitte schaut auf meine Webseite um ein Gefühl dafür zu bekommen wie viel Platz für Text vorhanden sein muss.

```html
<!DOCTYPE html>
<html lang="de">
<head>
<meta charset="utf-8">
<title>Sternzertifikat</title>
<link rel="stylesheet" href="https://fonts.googleapis.com/css2?family=Great+Vibes&family=Montserrat:wght@300&display=swap">
<style>
  :root {
    --paper: #ffffff;
    --ink: #1a1a1a;
    --rule: #6d6d6d;
    --seal-navy: #26306b;
    --sky-deep: #1f2a5c;
    --sky-mid: #3a4a8c;
    --sky-violet: #5b4a8f;
    --sky-rose: #a07bb0;
  }
  * { margin: 0; padding: 0; box-sizing: border-box; }
  html, body {
    width: 1200px;
    height: 773px;
    overflow: hidden;
    background: var(--paper);
  }
  .certificate {
    position: relative;
    width: 1200px;
    height: 773px;
    background: var(--paper);
    color: var(--ink);
    font-family: "Montserrat", sans-serif;
    font-weight: 300;
  }
  .night-sky {
    position: absolute;
    left: 88px;
    top: 107px;
    width: 544px;
    height: 544px;
    border-radius: 50%;
    background:
      radial-gradient(circle at 45% 62%, rgba(170, 180, 220, 0.55) 0%, rgba(120, 130, 190, 0.15) 28%, transparent 45%),
      radial-gradient(circle at 75% 85%, var(--sky-rose) 0%, transparent 40%),
      linear-gradient(150deg, var(--sky-mid) 0%, var(--sky-deep) 35%, var(--sky-violet) 75%, var(--sky-rose) 100%);
  }
  .info {
    position: absolute;
    left: 700px;
    top: 0;
    width: 430px;
    height: 773px;
    text-align: center;
  }
  .seal {
    position: absolute;
    left: 183px;
    top: 82px;
    width: 64px;
    height: 64px;
  }
  .title {
    position: absolute;
    left: 0;
    top: 162px;
    width: 100%;
    font-family: "Great Vibes", cursive;
    font-weight: 400;
    font-size: 76px;
    line-height: 1.1;
    letter-spacing: 1px;
  }
  .divider {
    position: absolute;
    left: 61px;
    top: 294px;
    width: 311px;
    height: 1px;
    background: var(--rule);
  }
  .entry {
    position: absolute;
    left: 0;
    top: 331px;
    width: 100%;
    font-size: 23px;
    line-height: 31.5px;
  }
  .register-number {
    position: absolute;
    left: 0;
    top: 612px;
    width: 100%;
    font-size: 23px;
    line-height: 31.5px;
  }
</style>
</head>
<body>
  <main class="certificate">
    <div class="night-sky" role="img" aria-label="Foto eines Sternenhimmels mit Milchstraße in Blau- und Violetttönen"></div>

    <section class="info">
      <svg class="seal" viewBox="0 0 64 64" aria-hidden="true">
        <circle cx="32" cy="32" r="31" fill="var(--seal-navy)"/>
      </svg>

      <h1 class="title">Sternzertifikat</h1>
      <div class="divider"></div>

      <p class="entry">
        Der Stern mit den Koordinaten<br>
        xx Koordinaten xx<br>
        wurde am 24.09.2022 in das<br>
        Sternenregister eingetragen.<br>
        Der Stern trägt den Namen
      </p>

      <p class="register-number">Die Registernummer lautet</p>
    </section>
  </main>
</body>
</html>
```